Flyer for swimming pool business

My company is R&T Bluewave. We do pool cleaning and maintenance services. We are entering our second season and want a nice flyer to solicit new business and mail to customers. Our slogan is "When you need your water bright, Call R&T Bluewave!" Maybe some package pricing options? I have a picture I use on the invoices which I have attached, you don't have to use it.
Please be creative, I'm looking for something original to stand out from all the other pool company's flyers in the area.

Please include the following as a list:
Weekly Maintenance & Vacuums
Pool Opening & Closings
Pump Repairs
Tile Cleaning
Acid Washes
Algae Removal
Heater Repair
Liner Repair
Leak Detection
One time clean ups

Last years flyer is attached below but I am looking for something different this year.
Updates

Please incorporate this into the flyer.

Pool Opening & Closings

Pump Repairs

Tile Cleaning

Acid Washes

Algae Removal

Heater Repair

Liner Repair

Leak Detection

One time clean ups

Target Market(s)

upper NY suburbs

Industry/Entity Type

Business

Requirements
Must have
• Our phone number 631-287-4150
water background
our slogan "When you need your water bright, Call R&T Bluewave!
our website www.CallBluewave.example
email: sales@CallBluewave.example

```html
<!DOCTYPE html>
<html lang="en">
<head>
<meta charset="utf-8">
<title>R&amp;T Bluewave – Pool Services Flyer</title>
<link rel="stylesheet" href="https://fonts.googleapis.com/css2?family=Arimo:wght@400;700&display=swap">
<style>
  :root {
    --tile: #d8d7cb;
    --grout: #b9b8ac;
    --coping: #8fa3b3;
    --water-light: #8ec9f0;
    --water-mid: #5aa9e6;
    --water-deep: #3c86d4;
    --wall: #2f72c8;
    --service-blue: #1946e6;
    --brand-blue: #a9d3ee;
    --slogan: #ffffff;
    --contact: #7d7d76;
    --contact-dark: #6a6a64;
  }
  html, body {
    margin: 0;
    padding: 0;
    overflow: hidden;
  }
  body {
    width: 810px;
    height: 1200px;
  }
  .flyer {
    position: relative;
    width: 810px;
    height: 1200px;
    overflow: hidden;
    font-family: "Arimo", Arial, sans-serif;
    background-color: var(--tile);
    background-image:
      linear-gradient(to right, var(--grout) 1px, transparent 1px),
      linear-gradient(to bottom, var(--grout) 1px, transparent 1px);
    background-size: 28.5px 28.5px;
    background-position: 4px 6px;
  }
  .pool-coping {
    position: absolute;
    left: 32px;
    top: 62px;
    width: 734px;
    height: 970px;
    box-sizing: border-box;
    border: 3px solid var(--coping);
    background:
      repeating-linear-gradient(to right, #c9d6df 0 3px, #9fb2c0 3px 4px);
    padding: 9px;
  }
  .pool-water {
    position: relative;
    width: 100%;
    height: 100%;
    background:
      linear-gradient(to left, var(--wall) 0 52px, transparent 52px),
      linear-gradient(to bottom, var(--water-deep) 0 14px, transparent 14px),
      radial-gradient(ellipse at 40% 45%, var(--water-light) 0%, var(--water-mid) 60%, var(--water-deep) 100%);
  }
  .services {
    position: absolute;
    top: 258px;
    left: 0;
    width: 810px;
    margin: 0;
    padding: 0;
    list-style: none;
    text-align: center;
  }
  .services li {
    font-weight: 700;
    font-size: 36px;
    line-height: 53.5px;
    color: var(--service-blue);
    letter-spacing: -0.2px;
  }
  .brand {
    position: absolute;
    left: 0;
    width: 810px;
    top: 900px;
    text-align: center;
  }
  .brand-name {
    margin: 0;
    font-weight: 700;
    font-size: 75px;
    line-height: 72px;
    color: var(--brand-blue);
    opacity: 0.9;
    letter-spacing: 0.5px;
  }
  .brand-slogan {
    margin: 4px 0 0;
    font-size: 15.5px;
    color: var(--slogan);
    letter-spacing: 3.2px;
  }
  .contact {
    position: absolute;
    left: 0;
    width: 810px;
    top: 1035px;
    text-align: center;
    color: var(--contact);
  }
  .contact-company {
    margin: 0;
    font-weight: 700;
    font-size: 14px;
    color: var(--contact-dark);
  }
  .contact-person {
    margin: 3px 0 0;
    font-weight: 700;
    font-size: 11px;
    color: var(--contact-dark);
  }
  .contact-phone {
    margin: 22px 0 0;
    font-size: 22px;
    color: var(--contact);
  }
  .contact-web,
  .contact-email {
    margin: 2px 0 0;
    font-size: 13.5px;
    color: var(--contact-dark);
  }
</style>
</head>
<body>
  <main class="flyer">
    <div class="pool-coping">
      <div class="pool-water" role="img" aria-label="Overhead photo of sparkling blue pool water with light ripples"></div>
    </div>

    <ul class="services">
      <li>Weekly Maintenance &amp; Vacuums</li>
      <li>Pool Opening &amp; Closing</li>
      <li>Pump Repairs</li>
      <li>Tile Cleaning</li>
      <li>Acid Waves</li>
      <li>Algae Removal</li>
      <li>Heater Repair</li>
      <li>Liner Repair</li>
      <li>Leak Detection</li>
      <li>One time clean ups</li>
    </ul>

    <header class="brand">
      <h1 class="brand-name">R&amp;T BLUEWAVE</h1>
      <p class="brand-slogan">When you need your water bright, Call R&amp;T Bluewave</p>
    </header>

    <footer class="contact">
      <p class="contact-company">R&amp;T BLUEWAVE</p>
      <p class="contact-person">Danny Marsh</p>
      <p class="contact-phone">Phone Number 631 - 287 - 4150</p>
      <p class="contact-web">www.CallBluewave.example</p>
      <p class="contact-email">sales@CallBluewave.example</p>
    </footer>
  </main>
</body>
</html>
```